Business Card Design

Velora Pixel Outreach

An online marketing consulting & strategy business for the cosmetic niche

We specialise in Increasing Leads, Conversions & Content Marketing

I am looking for a very clean, BOLD business card that is simple & effective

Target Market(s)

cosmetic surgeons & cosmetic clinics

Industry/Entity Type

Marketing

Contact Information for Business Card

Brett Kaminski
Online Marketing Strategist

Brett@VeloraPixelOutreach.example
0491 268 530

LinkedIn: in/brettkaminski

```html
<!DOCTYPE html>
<html lang="en">
<head>
<meta charset="utf-8">
<title>Velora Pixel Outreach — Business Card</title>
<link rel="stylesheet" href="https://fonts.googleapis.com/css2?family=Michroma&family=Roboto:wght@400;500;700&display=swap">
<style>
  :root {
    --stage: #d6d6d6;
    --card: #ffffff;
    --ink: #5c5e62;
    --blue: #2a9fd8;
    --teal: #55b3b0;
    --green: #8dc63f;
    --faint-green: rgba(141, 198, 63, 0.16);
    --faint-blue: rgba(42, 159, 216, 0.14);
    --card-radius: 26px;
  }
  * { box-sizing: border-box; margin: 0; padding: 0; }
  html, body {
    width: 1200px; height: 985px; overflow: hidden;
    background: var(--stage);
    font-family: "Roboto", Arial, sans-serif;
  }
  .canvas { position: relative; width: 1200px; height: 985px; }

  .card {
    position: absolute; left: 224px; width: 752px; height: 430px;
    background: var(--card); border-radius: var(--card-radius);
    overflow: hidden;
  }
  .card--back { top: 40px; }
  .card--front { top: 515px; }

  .wordmark {
    position: absolute;
    font-family: "Michroma", "Arial", sans-serif;
    font-weight: 400; color: var(--ink);
    text-transform: uppercase; line-height: 1.02;
    letter-spacing: 0.08em;
  }

  /* Back */
  .back-ring {
    position: absolute; left: 60px; top: -120px;
    width: 470px; height: 470px; border-radius: 50%;
    border: 60px solid var(--faint-green);
  }
  .back-mark {
    position: absolute; left: 300px; top: 178px;
    width: 72px; height: 72px; border-radius: 50%;
    background: var(--green);
  }
  .card--back .wordmark { left: 390px; top: 180px; font-size: 30px; }
  .back-band {
    position: absolute; left: 270px; right: 0; bottom: 0; height: 44px;
    border-top-left-radius: 22px;
    background: linear-gradient(90deg, var(--teal), var(--green));
    color: #fff; display: flex; align-items: center; padding-left: 26px;
    font-size: 20px; font-weight: 700; gap: 10px;
  }
  .back-band .role { font-weight: 400; font-size: 16px; border-left: 2px solid #fff; padding-left: 10px; }

  /* Front */
  .front-ring {
    position: absolute; right: -90px; top: 60px;
    width: 480px; height: 480px; border-radius: 50%;
    border: 60px solid var(--faint-blue);
  }
  .front-panel {
    position: absolute; left: 0; top: 0; bottom: 0; width: 240px;
    background: linear-gradient(180deg, var(--blue) 0%, var(--teal) 45%, var(--green) 100%);
  }
  .front-rule {
    position: absolute; left: 256px; top: 0; bottom: 0; width: 3px;
    background: var(--blue);
  }
  .front-mark {
    position: absolute; left: 150px; top: 34px;
    width: 150px; height: 130px; background: #fff;
  }
  .card--front .wordmark { left: 320px; top: 40px; font-size: 36px; }
  .person { position: absolute; left: 290px; top: 188px; }
  .person-name { font-size: 32px; font-weight: 700; }
  .person-name .first { color: var(--blue); }
  .person-name .last { color: var(--green); }
  .person-role {
    font-size: 21px; font-weight: 500; color: var(--green);
    padding-bottom: 6px; border-bottom: 2px solid var(--teal); width: 300px;
  }
  .contacts { position: absolute; left: 290px; top: 290px; list-style: none; }
  .contacts li {
    display: flex; align-items: center; gap: 14px;
    font-size: 20px; color: var(--ink); margin-bottom: 14px;
  }
  .contact-icon {
    width: 28px; height: 28px; background: var(--blue); border-radius: 4px;
    display: flex; align-items: center; justify-content: center;
  }
</style>
</head>
<body>
<main class="canvas">

  <section class="card card--back" aria-label="Business card back">
    <div class="back-ring"></div>
    <div class="back-mark"></div>
    <div class="wordmark">Velora<br>Pixel<br>Outreach</div>
    <div class="back-band"><span class="name">Brett Kaminski</span><span class="role">Online Marketing Strategist</span></div>
  </section>

  <section class="card card--front" aria-label="Business card front">
    <div class="front-ring"></div>
    <div class="front-panel"></div>
    <div class="front-rule"></div>
    <div class="front-mark"></div>
    <div class="wordmark">Velora<br>Pixel<br>Outreach</div>
    <div class="person">
      <p class="person-name"><span class="first">Brett</span> <span class="last">Kaminski</span></p>
      <p class="person-role">Online Marketing Strategist</p>
    </div>
    <ul class="contacts">
      <li>
        <span class="contact-icon">
          <svg width="16" height="16" viewBox="0 0 24 24"><path fill="#fff" d="M6.6 10.8a15.1 15.1 0 0 0 6.6 6.6l2.2-2.2a1 1 0 0 1 1-.25 11.4 11.4 0 0 0 3.6.57 1 1 0 0 1 1 1V20a1 1 0 0 1-1 1A17 17 0 0 1 3 4a1 1 0 0 1 1-1h3.5a1 1 0 0 1 1 1c0 1.25.2 2.45.57 3.57a1 1 0 0 1-.25 1z"/></svg>
        </span>0491 268 530
      </li>
      <li>
        <span class="contact-icon">
          <svg width="18" height="14" viewBox="0 0 18 14"><rect x="1" y="1" width="16" height="12" fill="none" stroke="#fff" stroke-width="1.6"/><path d="M1 1l8 7 8-7" fill="none" stroke="#fff" stroke-width="1.6"/></svg>
        </span>Brett@VeloraPixelOutreach.example
      </li>
      <li>
        <span class="contact-icon"></span>in/brettkaminski
      </li>
    </ul>
  </section>

</main>
</body>
</html>
```